" TRABALHAMOS NO SEGMENTO DE CAR CARE, COM VARIOS SERVIÇOS ESPECÍFICOS, COMO POLIMENTOS TÉCNICO, CERAMIC COATING, FULL DETAIL, RECUPERÇÃO DE VÁRIAS PARTES DOS VEÍCULOS E ETC... "

```html
<!DOCTYPE html>
<html lang="pt">
<head>
<meta charset="utf-8">
<title>Prime Gloss – Ceramic Coating</title>
<link rel="stylesheet" href="https://fonts.googleapis.com/css2?family=Montserrat:wght@400;500;700;800;900&display=swap">
<style>
  :root{
    --page:#e9e9e9;
    --black:#0d0d0d;
    --panel:#161616;
    --silver-light:#d9d9d9;
    --silver:#9a9a9a;
    --silver-dark:#5a5a5a;
    --white:#ffffff;
    --grey-text:#bdbdbd;
  }
  *{margin:0;padding:0;box-sizing:border-box}
  html,body{width:1200px;height:1200px;overflow:hidden;background:var(--page)}
  body{font-family:"Montserrat",Arial,sans-serif;color:var(--white)}
  .flyer{position:absolute;left:185px;top:15px;width:830px;height:1170px;background:var(--black);overflow:hidden}

  .header{position:absolute;left:0;top:0;width:100%;height:150px;background:linear-gradient(180deg,#1c1c1c,var(--black));display:flex;align-items:center;justify-content:center;gap:14px}
  .brand-dot{width:22px;height:22px;border-radius:50%;background:var(--white)}
  .brand-name{font-weight:900;font-size:44px;letter-spacing:2px;color:var(--white)}

  .hero-photo{position:absolute;left:0;top:150px;width:100%;height:560px;
    background:radial-gradient(ellipse at 75% 60%,#4a4a4a 0%,#262626 45%,#0e0e0e 80%),linear-gradient(90deg,#777 0%,#3a3a3a 40%,#111 100%);
    background-blend-mode:multiply}
  .headline{position:absolute;left:40px;top:190px;text-transform:uppercase;line-height:1}
  .headline .big{display:block;font-weight:900;font-size:68px;letter-spacing:1px;color:var(--white)}
  .headline .small{display:block;font-weight:700;font-size:32px;margin:8px 0 6px;color:var(--white)}
  .headline .tag{display:inline-block;font-weight:800;font-size:34px;padding:6px 14px;background:var(--black);color:var(--white);margin-bottom:8px}

  .stripes{position:absolute;left:0;top:690px;width:100%;height:80px}

  .info{position:absolute;left:0;top:760px;width:100%;height:320px;background:var(--panel)}
  .texture{position:absolute;left:35px;top:650px;width:320px;height:320px;border-radius:50%;
    border:10px solid var(--black);background:radial-gradient(circle at 40% 40%,#c8d0cf,#8e9998 60%,#5d6766);box-shadow:0 0 0 3px var(--silver)}
  .info-text{position:absolute;left:380px;top:790px;width:420px;text-align:center;text-transform:uppercase}
  .info-text .lead{font-weight:700;font-size:15px;line-height:1.35}
  .info-text .sub{font-weight:800;font-size:14px;margin:18px 0 10px}
  .features{list-style:none;font-weight:400;font-size:15px;line-height:1.55;color:var(--grey-text);text-transform:none}

  .footer{position:absolute;left:0;bottom:0;width:100%;height:90px;background:var(--black);border-top:3px solid var(--silver-dark);display:flex;align-items:center;justify-content:space-between;padding:0 40px}
  .site{font-weight:800;font-size:30px;letter-spacing:1px;color:var(--white);text-transform:uppercase}
  .footer-brand{display:flex;align-items:center;gap:8px;font-weight:900;font-size:20px}
  .footer-brand .brand-dot{width:12px;height:12px}
</style>
</head>
<body>
  <main class="flyer">
    <header class="header">
      <span class="brand-dot"></span>
      <span class="brand-name">PRIME GLOSS</span>
    </header>

    <div class="hero-photo" role="img" aria-label="Photo of a hand applying ceramic coating to a glossy black car near the headlight"></div>

    <h1 class="headline">
      <span class="big">Pioneiros</span>
      <span class="small">em aplicação de</span>
      <span class="tag">Ceramic Coating</span>
      <span class="big">Nesse País</span>
    </h1>

    <svg class="stripes" viewBox="0 0 830 80" preserveAspectRatio="none" aria-hidden="true">
      <defs>
        <linearGradient id="metal" x1="0" y1="0" x2="1" y2="0">
          <stop offset="0" stop-color="#5a5a5a"/>
          <stop offset="0.5" stop-color="#e0e0e0"/>
          <stop offset="1" stop-color="#6a6a6a"/>
        </linearGradient>
      </defs>
      <polygon points="0,40 830,10 830,30 0,60" fill="url(#metal)"/>
      <polygon points="0,62 830,32 830,80 0,80" fill="#161616"/>
    </svg>

    <section class="info">
    </section>
    <div class="texture" role="img" aria-label="Close-up photo of a grey microfiber polishing cloth"></div>

    <div class="info-text">
      <p class="lead">Coatings são proteções para superfícies das viaturas com dimensões nano tecnológicas, a proporcionar proteção mecânica, química e física, sem modificar as características originais.</p>
      <p class="sub">Suas principais características são:</p>
      <ul class="features">
        <li>Brilho intenso</li>
        <li>Efeito hidrofóbico (opcional)</li>
        <li>Auto Limpeza (antiestático)</li>
        <li>Ancoragem (de 6 meses até 5 anos)</li>
        <li>Dureza (9H)</li>
      </ul>
    </div>

    <footer class="footer">
      <span class="site">www.primegloss.com</span>
      <span class="footer-brand"><span class="brand-dot"></span>PRIME GLOSS</span>
    </footer>
  </main>
</body>
</html>
```